Sol Bocado Digital Menu Boards

IF SELECTED, WINNER MAY BE HIRED FOR OTHER DESIGNS OF DIFFERENT STORES OF OUR COMPANY.

Task: Digital Menu Boards Design

Task description: We need designs for a Digital Menu to be displayed on two 42’’screens at Solbocado, a fast-food restaurant in Guadalajara, Mexico. The menu redesign should communicate to our customers the experience of eating at our restaurant.

For avoiding the creation of videos, we are expecting several menu slides with the same text but with different images, simulating the effect of a video where the images are changing. This menu slides will be projected through a USB memory and a slideshow.

Attached files:
For the design, there are several documents attached to the task description:
1. Logo of the restaurant
2. Pictures of the restaurant
3. Example video of what we want to achieve through this menu slides.
4. Pictures of the actual menu board, to be replaced with the new designs.
5. Menu description (regular and breakfast menu)
6. Pictures of each element on the menu (We don’t have yet any breakfast pictures)
**The files are organized on a ZIP file.

Expected product:
For the regular menu,
• 2 menu slide designs for TACOS Y ESPECIALIDADES, where the text will be exactly the same but the images would differ.
• 2 menu slide designs for BEBIDAS Y EXTRAS, where the text will be exactly the same but the images would differ.
For the breakfast menu,
• 1 menu slide including all the menu
Total: 5 menu board slides.

Technical specs:
• You should send the editable file, med and high resolution JPGs for each design.
• The designs should fit perfectly on 42’’ screens.

Reason: Designers, For the final decision we are asking for a minimum of designs for chosing, we are going to wait a little bit more. Solbocado

Industry/Entity Type

Restaurant

```html
<!DOCTYPE html>
<html lang="es">
<head>
<meta charset="utf-8">
<title>Sol Bocado — Tacos y Especialidades</title>
<link rel="stylesheet" href="https://fonts.googleapis.com/css2?family=Lobster&family=Roboto+Condensed:wght@400;700&display=swap">
<style>
  :root {
    --board-dark: #5a1a12;
    --board-mid: #8e2a1c;
    --board-light: #a8382a;
    --paper-light: #f3c98c;
    --paper-dark: #c9833f;
    --card-frame: #f5cf92;
    --panel: #ffffff;
    --label-teal: #7dbdb1;
    --ink: #1f1f1f;
    --price-red: #c8102e;
    --title-white: #ffffff;
    --title-red: #c3102a;
    --photo-warm: #d9b48a;
    --photo-cream: #efe2c8;
    --photo-meat: #9c5a3c;
    --photo-green: #9fb84a;
    --photo-salsa: #d9503a;
  }
  * { margin: 0; padding: 0; box-sizing: border-box; }
  html, body { width: 1200px; height: 669px; overflow: hidden; }
  body { font-family: "Roboto Condensed", "Arial Narrow", sans-serif; }

  .menu-board {
    position: relative;
    width: 1200px;
    height: 669px;
    overflow: hidden;
    background:
      radial-gradient(ellipse at 50% 45%, var(--board-light) 0%, var(--board-mid) 45%, var(--board-dark) 100%);
  }

  .title-band {
    position: absolute;
    left: 18px; top: 106px;
    width: 900px; height: 148px;
    background: linear-gradient(180deg, var(--paper-light) 0%, #e6aa62 55%, var(--paper-dark) 100%);
    clip-path: polygon(0 8%, 12% 4%, 30% 7%, 48% 2%, 66% 6%, 84% 1%, 100% 5%, 99% 92%, 80% 97%, 60% 93%, 40% 99%, 20% 94%, 1% 98%);
  }
  .title-band__text {
    position: absolute;
    left: 40px; top: 128px;
    width: 780px;
    text-align: center;
    font-family: "Lobster", cursive;
    font-weight: 400;
    font-size: 84px;
    line-height: 1;
    color: var(--title-white);
    -webkit-text-stroke: 3px var(--title-red);
    paint-order: stroke fill;
    text-shadow: 3px 4px 0 var(--title-red);
  }

  .brand {
    position: absolute;
    left: 910px; top: 14px;
    width: 256px; height: 256px;
    border-radius: 50%;
    background: var(--card-frame);
    display: flex;
    align-items: center;
    justify-content: center;
  }
  .brand__name {
    font-weight: 700;
    font-size: 42px;
    line-height: 1;
    color: var(--price-red);
    white-space: nowrap;
  }

  .menu-card {
    position: absolute;
    top: 291px;
    width: 522px; height: 316px;
    background: var(--card-frame);
    border-radius: 26px;
    box-shadow: 0 4px 10px rgba(0,0,0,.35);
  }
  .menu-card--quesadilla { left: 64px; }
  .menu-card--gringa { left: 608px; }

  .menu-card__photo {
    position: absolute;
    left: 240px; top: 14px;
    width: 268px; height: 290px;
    border-radius: 6px 20px 20px 6px;
  }
  .menu-card--quesadilla .menu-card__photo {
    background:
      radial-gradient(ellipse 60% 30% at 60% 30%, var(--photo-meat) 0%, rgba(156,90,60,0) 100%),
      radial-gradient(ellipse 70% 30% at 50% 75%, #c48a78 0%, rgba(196,138,120,0) 100%),
      linear-gradient(170deg, #f7f3ec 0%, var(--photo-cream) 45%, var(--photo-warm) 100%);
  }
  .menu-card--gringa .menu-card__photo {
    background:
      radial-gradient(ellipse 45% 22% at 25% 12%, var(--photo-green) 0%, rgba(159,184,74,0) 100%),
      radial-gradient(ellipse 45% 25% at 80% 18%, var(--photo-salsa) 0%, rgba(217,80,58,0) 100%),
      radial-gradient(ellipse 80% 25% at 55% 85%, #c77a45 0%, rgba(199,122,69,0) 100%),
      linear-gradient(175deg, #f7f3ec 0%, var(--photo-cream) 55%, #e3c79a 100%);
  }

  .menu-card__panel {
    position: absolute;
    left: 13px; top: 13px;
    width: 237px; height: 291px;
    background: var(--panel);
    border-radius: 22px;
    overflow: hidden;
    box-shadow: 3px 0 6px rgba(0,0,0,.2);
    text-align: center;
    color: var(--ink);
  }
  .menu-card__label {
    height: 52px;
    margin-top: 5px;
    background: var(--label-teal);
    border-radius: 20px 20px 0 0;
    font-weight: 700;
    font-size: 35px;
    line-height: 52px;
  }
  .menu-item {
    font-size: 35px;
    line-height: 1;
  }
  .menu-item__price {
    display: block;
    font-weight: 700;
    font-size: 48px;
    color: var(--price-red);
    margin-top: 2px;
  }
  .menu-card__items { padding-top: 8px; }
  .menu-card__items .menu-item + .menu-item { margin-top: 6px; }
  .menu-card--gringa .menu-card__items { padding-top: 50px; }

  .menu-card__extra {
    position: absolute;
    left: 0; right: 0; bottom: 8px;
    font-size: 20px;
    line-height: 1.1;
  }
  .menu-card__extra strong {
    display: block;
    color: var(--price-red);
    font-size: 19px;
  }
</style>
</head>
<body>
<main class="menu-board">
  <div class="title-band" role="img" aria-label="Franja de papel rústico"></div>
  <h1 class="title-band__text">Tacos y Especialidades</h1>

  <div class="brand">
    <span class="brand__name">Sol Bocado</span>
  </div>

  <section class="menu-card menu-card--quesadilla">
    <div class="menu-card__photo" role="img" aria-label="Fotografía de quesadillas de pastor y arrachera con queso fundido"></div>
    <div class="menu-card__panel">
      <h2 class="menu-card__label">QUESADILLA</h2>
      <div class="menu-card__items">
        <p class="menu-item">PASTOR <span class="menu-item__price">18</span></p>
        <p class="menu-item">ARRACHERA <span class="menu-item__price">20</span></p>
      </div>
      <p class="menu-card__extra">TORTILLA DE HARINA <strong>+1 PESO</strong></p>
    </div>
  </section>

  <section class="menu-card menu-card--gringa">
    <div class="menu-card__photo" role="img" aria-label="Fotografía de gringa de pastor con guacamole y pico de gallo"></div>
    <div class="menu-card__panel">
      <h2 class="menu-card__label">GRINGA</h2>
      <div class="menu-card__items">
        <p class="menu-item">PASTOR <span class="menu-item__price">20</span></p>
      </div>
      <p class="menu-card__extra">TORTILLA DE HARINA <strong>+2 PESOS</strong></p>
    </div>
  </section>
</main>
</body>
</html>
```